Dallas Texas Special Event Center Flyer

Need a new brochure (small 8.5 x 11 tri-fold) for an event center in Dallas, Texas area. It is located on a golf course and is ideal for weddings, quinceaneras, retirement parties, etc. Is best known for weddings. There is no logo for the event center. I have attached the prior brochure, which is not professional. We do not have any site photos.

Target Market(s)

people seeking special event space in dallas, texas area. Brides, meeting planners, etc.

Industry/Entity Type

Golf Course

Font styles to use
Script
Other font styles liked:
• combine serif and some use of script ok

Requirements
Must have
• lots of photos - see attached

```html
<!DOCTYPE html>
<html lang="en">
<head>
<meta charset="utf-8">
<title>Willowmere Hall – Tri-fold Brochure</title>
<link href="https://fonts.googleapis.com/css2?family=Lobster&family=Open+Sans:wght@400;600&display=swap" rel="stylesheet">
<style>
  :root {
    --blush: #e6b4a2;
    --blush-deep: #dba592;
    --mauve: #a9566f;
    --white: #ffffff;
    --body-text: #5b3a35;
    --page-bg: #e9e7e5;
    --script: "Lobster", cursive;
    --sans: "Open Sans", Arial, sans-serif;
  }
  * { box-sizing: border-box; margin: 0; padding: 0; }
  html, body { width: 1200px; height: 532px; overflow: hidden; }
  body { background: var(--page-bg); position: relative; font-family: var(--sans); }

  .spread { position: absolute; top: 31px; width: 577px; height: 444px; background: var(--blush); box-shadow: 0 2px 8px rgba(0,0,0,.18); }
  .spread--outside { left: 19px; }
  .spread--inside { left: 608px; }

  .panel { position: absolute; top: 0; width: 193px; height: 444px; }
  .panel--1 { left: 0; }
  .panel--2 { left: 192px; }
  .panel--3 { left: 384px; }

  .header { height: 98px; background: var(--blush); text-align: center; display: flex; align-items: center; justify-content: center; }
  .venue-name { font-family: var(--sans); font-weight: 600; font-size: 25px; line-height: 1.15; color: var(--white); }
  .contact-head { color: var(--white); font-family: var(--script); font-size: 17px; line-height: 1.12; padding: 0 26px; }

  .photo { position: absolute; }
  .photo--bride-window { left: 0; top: 98px; width: 192px; height: 346px;
    background: linear-gradient(160deg, #5d6a55 0%, #8c8f80 35%, #b8b3ab 60%, #6f6a62 100%); }
  .photo--centerpiece { left: 192px; top: 98px; width: 385px; height: 346px;
    background: radial-gradient(ellipse at 70% 75%, #6d7d3e 0%, #a07a4e 35%, transparent 65%),
                linear-gradient(180deg, #d9a56a 0%, #c48350 40%, #8a5a38 100%); }

  .intro { position: absolute; left: 18px; right: 18px; top: 206px; text-align: center; color: var(--white);
    font-family: var(--script); font-size: 12px; line-height: 1.3; text-shadow: 0 1px 2px rgba(0,0,0,.35); }

  .contact { position: absolute; left: 0; top: 110px; width: 193px; text-align: center; color: var(--white); text-shadow: 0 1px 2px rgba(0,0,0,.35); font-family: var(--script); }
  .contact .web { font-size: 11.5px; }
  .contact .name { font-size: 17px; margin-top: 8px; }
  .contact .email { font-size: 11px; }
  .contact .phone { font-size: 18px; line-height: 1.1; margin-top: 3px; }

  .address-ribbon { position: absolute; left: 10px; top: 218px; width: 176px; height: 68px; }
  .address-ribbon svg { position: absolute; inset: 0; }
  .address-ribbon .text { position: absolute; inset: 0; padding-top: 6px; text-align: center; color: var(--white); font-family: var(--script); line-height: 1.15; }
  .address-ribbon .venue { font-size: 12px; }
  .address-ribbon .street { font-size: 16.5px; }

  .tagline { position: absolute; left: 22px; right: 22px; top: 112px; text-align: center; color: var(--mauve);
    font-family: var(--script); font-size: 18px; line-height: 1.22; }

  .inside-text { background: var(--blush-deep); height: 444px; }
  .inside-text .header { background: transparent; }
  .divider { display: block; margin: 0 auto 6px; }
  .body-copy { padding: 0 22px; color: var(--body-text); font-size: 7px; line-height: 1.25; text-align: center; }
  .body-copy p + p { margin-top: 6px; }

  .gallery { position: absolute; left: 192px; top: 0; width: 385px; height: 444px; background: var(--white); }
  .tile { position: absolute; }
  .tile--toast     { left: 0;   top: 0;   width: 205px; height: 168px; background: linear-gradient(135deg, #c9b89c, #8d7055 60%, #3e3a38); }
  .tile--roses     { left: 207px; top: 0; width: 178px; height: 121px; background: linear-gradient(160deg, #f2ecea, #e8c8cc 55%, #dcd6d0); }
  .tile--couple    { left: 207px; top: 123px; width: 178px; height: 122px; background: linear-gradient(140deg, #8aa15a, #d9c9b6 55%, #f1ece6); }
  .tile--mic       { left: 0;   top: 170px; width: 112px; height: 75px; background: linear-gradient(135deg, #7c6c5c, #b9a48d 60%, #4e453d); }
  .tile--table     { left: 114px; top: 170px; width: 91px; height: 75px; background: linear-gradient(160deg, #e9e4e0, #c9aeb3 60%, #8b7f77); }
  .tile--cake      { left: 0;   top: 247px; width: 205px; height: 116px; background: linear-gradient(160deg, #f2c6b6, #f1e3c7 50%, #e7b3a6); }
  .tile--bouquets  { left: 207px; top: 247px; width: 178px; height: 82px; background: linear-gradient(150deg, #e8c2c0, #f4efe8 55%, #d9b2ad); }
  .tile--veil      { left: 0;   top: 365px; width: 58px; height: 79px; background: linear-gradient(160deg, #d8d0cb, #9a8e88); }
  .tile--lace      { left: 60px; top: 365px; width: 145px; height: 79px; background: linear-gradient(150deg, #e7d4cd, #c8948a 55%, #efe4de); }
  .tile--cake-cut  { left: 207px; top: 331px; width: 178px; height: 113px; background: linear-gradient(150deg, #b7b0ab, #f0ebe6 50%, #d6a3a8); }
</style>
</head>
<body>

<section class="spread spread--outside">
  <div class="panel panel--1">
    <div class="header"><h2 class="venue-name">Willowmere<br>Hall</h2></div>
    <div class="photo photo--bride-window" role="img" aria-label="Soft-focus photo of a bride standing by a sunlit window"></div>
    <p class="intro">Willowmere Hall is located on Willowmere Golf Course, an 18-hole, 215-acre championship golf course in Fernhill, Texas and is surrounded by rolling hills, seven beautiful lakes, creeks, pecan orchards and many varieties of wildlife.</p>
  </div>

  <div class="photo photo--centerpiece" role="img" aria-label="Photo of a floral centerpiece with roses and greenery on a candlelit banquet table"></div>

  <div class="panel panel--2">
    <div class="header"><p class="contact-head">Contact us for more information or visit us at:</p></div>
    <div class="contact">
      <p class="web">www.willowmerehall.com</p>
      <p class="name">Carol Whitman</p>
      <p class="email">carol@willowmerehall.com</p>
      <p class="phone">214-555-0142<br>972-555-0187</p>
    </div>
    <div class="address-ribbon">
      <svg width="176" height="68" viewBox="0 0 176 68" aria-hidden="true">
        <polygon points="0,0 176,0 165,34 176,68 0,68 11,34" fill="var(--mauve)"/>
      </svg>
      <div class="text">
        <p class="venue">Willowmere Hall</p>
        <p class="street">1820 E Highway 90<br>Fernhill, TX 75000</p>
      </div>
    </div>
  </div>

  <div class="panel panel--3">
    <div class="header"><h2 class="venue-name">Willowmere<br>Hall</h2></div>
    <p class="tagline">Host your event at the Dallas area’s premiere event venue</p>
  </div>
</section>

<section class="spread spread--inside">
  <div class="panel panel--1 inside-text">
    <div class="header"><h2 class="venue-name">Willowmere<br>Hall</h2></div>
    <svg class="divider" width="40" height="8" viewBox="0 0 40 8" aria-hidden="true">
      <line x1="2" y1="4" x2="38" y2="4" stroke="var(--white)" stroke-width="1.4"/>
    </svg>
    <div class="body-copy">
      <p>Willowmere Hall offers a 12,000 square foot facility which boasts a Grand Ballroom and two Banquet rooms.</p>
      <p>The grand ballroom will accommodate 809 guests for a wedding ceremony and reception, quinceanera, retirement party or any occasion that demands a large-scale, elegant setting.</p>
      <p>The bridal suite at the top of the winding staircase allows the Bride and her bridesmaids to prepare for the big day out of sight of arriving guests, allowing a dramatic grand entrance.</p>
      <p>Banquet room 1 will accommodate 103 guests for a mid-size, private event such as a birthday or retirement party or company holiday party while Banquet room 2 will accommodate 35 guests for a small intimate event such as a bridal shower, bridesmaid’s luncheon or corporate training. The rooms can be used separately or together.</p>
      <p>The event center has a full commercial kitchen onsite to cater any event from formal dining to buffet-style. The menu can be customized to your specifications and will be prepared by our expert chef and his team.</p>
      <p>Willowmere Hall is the perfect location for your wedding, conference, seminar, party, reunion or graduation.</p>
    </div>
  </div>

  <div class="gallery">
    <div class="tile tile--toast" role="img" aria-label="Photo of wedding guests raising champagne glasses in a toast"></div>
    <div class="tile tile--roses" role="img" aria-label="Photo of pink and white rose arrangements on a reception table"></div>
    <div class="tile tile--couple" role="img" aria-label="Photo of a newlywed couple at an outdoor garden ceremony"></div>
    <div class="tile tile--mic" role="img" aria-label="Photo of a microphone in front of conference seating"></div>
    <div class="tile tile--table" role="img" aria-label="Photo of a banquet table with a floral centerpiece"></div>
    <div class="tile tile--cake" role="img" aria-label="Close-up photo of a wedding cake decorated with sugar roses"></div>
    <div class="tile tile--bouquets" role="img" aria-label="Photo of bridesmaids holding white bouquets"></div>
    <div class="tile tile--veil" role="img" aria-label="Photo of a bride's veil"></div>
    <div class="tile tile--lace" role="img" aria-label="Photo of a lace wedding dress being buttoned"></div>
    <div class="tile tile--cake-cut" role="img" aria-label="Photo of a couple cutting a tiered wedding cake"></div>
  </div>
</section>

</body>
</html>
```